依頼詳細
現状はデザインの入ったアルミパックとなっておりますが、今回デザインした箱に無地のアルミパックを入れる方向に転換したいと思っておりますので、箱のデザインを依頼したいと思います。しかしながら、アルミパックのままデザインのみ変更する場合も考えられますので、どちらでも使えるデザインだと大変助かります。
記載項目
現状サイズ:たて約23cm×よこ約17cmのパック。
希望イメージ
シンプル 複雑
単色 カラフル
暗い 明るい
日常 高級
遊び心 厳粛
未来的 伝統的
女性的 男性的
希望する色
納品ファイル
• 高解像度JPG (.jpg)
• イラストレーター形式 (.ai)
補足説明
添付は現在の商品デザインになります。
皆様ご提案頂き誠にありがとうございます。
延長の理由を追記させて頂きます。
当方のイメージとしましては、全体的にもう少し「アート感」が欲しいところであります。
香川県はうどんだけでなく、直島などのアートの県としての特徴もございますので、その辺りを含んだデザインでお願い致します。
■ 選んだ理由

皆様たくさんのご提案誠にありがとうございました。
とても良いデザインが多いなか選考に時間がかかりましたが、個人的にパッと見たときのデザイン性、斬新さなどからこちらのデザインに決定させて頂きました。和をイメージして頂いたデザインも多かったですが、よくある和なイメージかなと思いましたのと、四国をイメージして頂いていたものも海外の方には分かりにくいかなと思い、今回のちょっと違った捉え方をした「和」とデザイン性(アート)の感じられたこちらのデザインに決定させて頂きました。皆様ご提案ありがとうございました。

■ 提案者全員のお礼・コメント

改めましてこの度は素晴らしいデザインのご提案、誠にありがとうございました。また早速コメントも返信頂きありがとうございます。後ほど一部修正案等まとめまして、ご相談させて頂きます。引き続きどうぞよろしくお願い致します。

```html
<!DOCTYPE html>
<html lang="ja">
<head>
<meta charset="utf-8">
<title>潮の香 無添加だしパック</title>
<link rel="stylesheet" href="https://fonts.googleapis.com/css2?family=Zen+Kaku+Gothic+New:wght@500;700;900&family=Zen+Maru+Gothic:wght@700;900&display=swap">
<style>
  :root {
    --paper: #ffffff;
    --ink: #1a1a1a;
    --frame: #b9b9b9;
    --wave-mint: #b9dfd6;
    --wave-sky: #8fb6e3;
    --wave-lilac: #a9a4dc;
    --wave-blue: #5f8fd2;
  }
  html, body {
    margin: 0;
    padding: 0;
    width: 889px;
    height: 1200px;
    overflow: hidden;
    background: var(--paper);
  }
  .package {
    position: relative;
    width: 889px;
    height: 1200px;
    box-sizing: border-box;
    border: 3px solid var(--frame);
    background: var(--paper);
    overflow: hidden;
    font-family: "Zen Kaku Gothic New", sans-serif;
    color: var(--ink);
  }
  .wave-field {
    position: absolute;
    left: 0;
    top: 110px;
    width: 100%;
    height: calc(100% - 110px);
    background:
      radial-gradient(ellipse 70% 55% at 50% 55%, rgba(255,255,255,0.55), rgba(255,255,255,0) 70%),
      linear-gradient(180deg, var(--paper) 0%, var(--wave-mint) 14%, var(--wave-sky) 40%, var(--wave-lilac) 62%, var(--wave-blue) 100%);
  }
  .vertical {
    position: absolute;
    writing-mode: vertical-rl;
    text-orientation: upright;
    margin: 0;
    line-height: 1;
  }
  .tag-additive-free {
    position: absolute;
    left: 712px;
    top: 44px;
    width: 72px;
    height: 342px;
    background: var(--ink);
    clip-path: polygon(0 0, 100% 0, 100% 82%, 50% 100%, 0 82%);
  }
  .tag-additive-free span {
    position: absolute;
    left: 50%;
    top: 22px;
    transform: translateX(-50%);
    writing-mode: vertical-rl;
    text-orientation: upright;
    color: var(--paper);
    font-weight: 700;
    font-size: 27px;
    letter-spacing: 1px;
  }
  .catch-copy {
    left: 618px;
    top: 135px;
    font-size: 34px;
    font-weight: 700;
    letter-spacing: 1px;
  }
  .product-name {
    left: 350px;
    top: 205px;
    font-family: "Zen Maru Gothic", sans-serif;
    font-weight: 900;
    font-size: 205px;
    letter-spacing: -8px;
  }
  .product-reading {
    left: 592px;
    top: 915px;
    font-size: 28px;
    font-weight: 500;
    letter-spacing: 4px;
  }
  .badge {
    position: absolute;
    width: 66px;
    background: var(--ink);
    clip-path: polygon(0 14px, 50% 0, 100% 14px, 100% 100%, 0 100%);
  }
  .badge span {
    position: absolute;
    left: 50%;
    top: 26px;
    transform: translateX(-50%);
    writing-mode: vertical-rl;
    text-orientation: upright;
    color: var(--paper);
    font-weight: 700;
    font-size: 36px;
    letter-spacing: 3px;
  }
  .badge-domestic { left: 224px; top: 160px; height: 168px; }
  .badge-natural { left: 150px; top: 176px; height: 240px; }
  .contents {
    left: 300px;
    top: 372px;
    font-size: 27px;
    font-weight: 700;
    letter-spacing: 1px;
  }
</style>
</head>
<body>
  <main class="package">
    <div class="wave-field" role="img" aria-label="青・ミント・薄紫の同心円の波紋模様"></div>

    <div class="tag-additive-free"><span>無添加だしパック</span></div>
    <p class="vertical catch-copy">こだわりのプロの味をご家庭に…</p>

    <h1 class="vertical product-name">潮の香</h1>
    <p class="vertical product-reading">しおのかおり</p>

    <div class="badge badge-domestic"><span>純国産</span></div>
    <div class="badge badge-natural"><span>天然素材</span></div>
    <p class="vertical contents">四人分のだし×20袋入り</p>
  </main>
</body>
</html>
```